Vex9Tax Business Card

Need a new business card for my law firm. The major components for the card will be my logo "Vex9Tax," the photo of me, contact information, and a QR Code for my website vex9tax.com. If you are unable to generate a QR Code, let me know and I'll see if I can make one. For the "Vex9Tax" logo, don't worry about the "Ride The Wave" part, you can leave that out. Here are my and the firm details:
Benedicto R Salazar III
Attorney at Law
Address: 250 Harbor Plaza, Suite 400
Dallas, TX 75201
Office #: 877-482-6173
Cell #: 214-657-3381
Fax #: 469-738-5126
Email: vex@vex9tax.com
Website: vex9tax.com

```html
<!DOCTYPE html>
<html lang="en">
<head>
<meta charset="utf-8">
<title>Vex9Tax Business Card</title>
<link rel="stylesheet" href="https://fonts.googleapis.com/css2?family=Open+Sans:wght@400;700;800&display=swap">
<style>
  :root {
    --backdrop: #4a4a4a;
    --card: #000000;
    --accent: #3cc3f2;
    --ink: #ffffff;
    --ink-soft: #e8e8e8;
    --photo-light: #2a2c33;
    --photo-dark: #050505;
  }
  * { box-sizing: border-box; margin: 0; padding: 0; }
  html, body {
    width: 1200px; height: 801px; overflow: hidden;
    background: var(--backdrop);
    font-family: "Open Sans", sans-serif;
  }
  .stage {
    position: relative; width: 1200px; height: 801px;
    display: flex; align-items: center; justify-content: center; gap: 40px;
  }
  .card {
    position: relative; width: 540px; height: 309px;
    background: var(--card); overflow: hidden;
  }
  .card--front { border-bottom: 2px solid var(--accent); border-right: 2px solid var(--accent); }
  .card--back { border-bottom: 2px solid var(--accent); border-left: 2px solid var(--accent); }

  .wordmark {
    font-family: "Open Sans", sans-serif; font-weight: 800;
    color: var(--ink); letter-spacing: 1px; line-height: 1;
  }

  .front-brand { position: absolute; left: 24px; top: 36px; }
  .front-brand .wordmark { font-size: 50px; }

  .accent-bar {
    position: absolute; left: 0; top: 122px; width: 10px; height: 30px;
    background: var(--accent);
  }
  .identity { position: absolute; left: 24px; top: 118px; }
  .identity .name { color: var(--accent); font-weight: 700; font-size: 18px; line-height: 1.2; }
  .identity .role { color: var(--ink); font-size: 11px; margin-top: 2px; }

  .address { position: absolute; left: 24px; top: 170px; color: var(--ink); font-size: 11px; line-height: 1.45; }

  .contacts { position: absolute; left: 24px; top: 212px; list-style: none; }
  .contacts li {
    display: flex; align-items: center; gap: 7px;
    color: var(--ink-soft); font-size: 11px; line-height: 16px;
  }
  .contacts svg { width: 11px; height: 11px; fill: none; stroke: var(--accent); stroke-width: 1.6; }

  .portrait {
    position: absolute; right: 20px; top: 18px; width: 230px; height: 270px;
    background: radial-gradient(ellipse at 50% 40%, var(--photo-light), var(--photo-dark) 70%);
  }

  .back-brand {
    position: absolute; inset: 0;
    display: flex; align-items: center; justify-content: center;
  }
  .back-brand .wordmark { font-size: 84px; }
</style>
</head>
<body>
<main class="stage">
  <section class="card card--front">
    <div class="front-brand">
      <div class="wordmark">Vex9Tax</div>
    </div>

    <span class="accent-bar"></span>
    <div class="identity">
      <p class="name">Benedicto R Salazar III</p>
      <p class="role">Attorney at Law</p>
    </div>

    <p class="address">250 Harbor Plaza,<br>Suite 400 Dallas, TX 75201</p>

    <ul class="contacts">
      <li><svg viewBox="0 0 12 12"><path d="M2 4.5C2 3 3 2 6 2s4 1 4 2.5L8.5 5 8 4H4L3.5 5Z M3 10V7h6v3Z"/></svg>877-482-6173</li>
      <li><svg viewBox="0 0 12 12"><rect x="3" y="1" width="6" height="10" rx="1"/><path d="M5 9h2"/></svg>214-657-3381</li>
      <li><svg viewBox="0 0 12 12"><rect x="1.5" y="5" width="9" height="6" rx="1"/><path d="M3.5 5V1.5h5V5 M3.5 7.5h5"/></svg>469-738-5126</li>
      <li><svg viewBox="0 0 12 12"><rect x="1" y="3" width="10" height="7" rx="1"/><path d="M1 3l5 4 5-4"/></svg>vex@vex9tax.com</li>
      <li><svg viewBox="0 0 12 12"><circle cx="6" cy="6" r="5"/><path d="M1 6h10 M6 1c-3 3-3 7 0 10 M6 1c3 3 3 7 0 10"/></svg>www.vex9tax.com</li>
    </ul>

    <div class="portrait" role="img" aria-label="Portrait photo of the attorney in a dark suit and light shirt against a black background"></div>
  </section>

  <section class="card card--back">
    <div class="back-brand">
      <div class="wordmark">Vex9Tax</div>
    </div>
  </section>
</main>
</body>
</html>
```